we need a design for Water Bottle Lable Wrap
The product is called Corvane Water is a restructured water. its a very healthy and rejuvenating water
we were looking at using as a tag ling Restore, Recover, Rejuvenate.

```html
<!DOCTYPE html>
<html lang="en">
<head>
<meta charset="UTF-8">
<title>Corvane Water – Label Wrap</title>
<link rel="stylesheet" href="https://fonts.googleapis.com/css2?family=Montserrat:wght@500;600&display=swap">
<style>
  :root {
    --canvas-bg: #ffffff;
    --label-bg: #ffffff;
    --brand-blue: #3fa3ee;
    --tagline-grey: #6b6b6b;
    --water-light: #e4f3fd;
    --water-mid: #9fd2f7;
    --water-deep: #3f9ff0;
    --bubble-faint: #d6ecfb;
  }
  * { margin: 0; padding: 0; box-sizing: border-box; }
  html, body {
    width: 1200px;
    height: 1200px;
    overflow: hidden;
    background: var(--canvas-bg);
  }
  .canvas {
    position: relative;
    width: 1200px;
    height: 1200px;
  }
  .label-wrap {
    position: absolute;
    left: 240px;
    top: 60px;
    width: 720px;
    height: 1080px;
    background: var(--label-bg);
    overflow: hidden;
  }
  .bubbles-scatter {
    position: absolute;
    left: 0;
    top: 0;
    width: 240px;
    height: 100%;
    background: linear-gradient(90deg, var(--bubble-faint) 0%, rgba(255,255,255,0) 100%);
  }
  .water-splash {
    position: absolute;
    right: 0;
    top: 0;
    width: 370px;
    height: 100%;
    background:
      radial-gradient(ellipse 38% 48% at 45% 55%, var(--water-deep) 0%, var(--water-mid) 55%, rgba(159,210,247,0) 100%),
      linear-gradient(90deg, rgba(228,243,253,0) 0%, var(--water-light) 35%, var(--water-mid) 100%);
  }
  .brand-name {
    position: absolute;
    left: 118px;
    top: 116px;
    height: 940px;
    writing-mode: vertical-rl;
    transform: rotate(180deg);
    font-family: "Montserrat", sans-serif;
    font-weight: 600;
    font-size: 212px;
    line-height: 180px;
    color: var(--brand-blue);
    text-align: right;
    letter-spacing: -4px;
  }
  .tagline {
    position: absolute;
    left: 314px;
    top: 290px;
    height: 500px;
    writing-mode: vertical-rl;
    transform: rotate(180deg);
    font-family: "Montserrat", sans-serif;
    font-weight: 500;
    font-size: 26px;
    line-height: 32px;
    letter-spacing: 1.5px;
    color: var(--tagline-grey);
    text-align: left;
    white-space: nowrap;
  }
</style>
</head>
<body>
  <main class="canvas">
    <section class="label-wrap">
      <div class="bubbles-scatter" role="img" aria-label="Scattered light blue water droplets"></div>
      <div class="water-splash" role="img" aria-label="Flowing blue water splash with bubbles"></div>
      <h1 class="brand-name">Corvane</h1>
      <p class="tagline">RESTORE, RECOVER, REJUVENATE</p>
    </section>
  </main>
</body>
</html>
```